Calvoreta Wine Label - Red Wine

We are a wine producing company based on the Oporto Metropolitan area.

We are looking to develop a label for a new red wine called "Calvoreta". Calvoreta is Portuguese for the well-known Spanish word Señorita, meaning a young lady. We want to make a label that reflects this young feeling with bright colours and fun designs while maintaining some elegance.

The target audience will be young people looking for a good time. Its preferred moments of consumption will be in social gatherings or fun times. We want to communicate fun.

We've attached the bottle model to be used, as well as some inspirational elements and our logo.
Updates

Low design quality

Target Market(s)

Young Consumers

Industry/Entity Type

Wine

Requirements
Must have
• Vintage year 2021, Red Wine mention

```html
<!DOCTYPE html>
<html lang="pt">
<head>
<meta charset="utf-8">
<title>Calvoreta – Wine Label</title>
<link rel="stylesheet" href="https://fonts.googleapis.com/css2?family=Sniglet&family=Montserrat:wght@500&family=Playfair+Display:wght@700&display=swap">
<style>
  :root {
    --backdrop: #8f8682;
    --paper: #ffffff;
    --wine-red: #d6233f;
    --wine-red-deep: #b81c33;
    --ink: #1a1a1a;
    --sketch-tone: #f1e6e8;
  }
  * { margin: 0; padding: 0; box-sizing: border-box; }
  html, body { width: 1200px; height: 816px; overflow: hidden; }
  body {
    background: var(--backdrop);
    display: flex;
    align-items: center;
    justify-content: center;
  }
  .label {
    position: relative;
    width: 600px;
    height: 740px;
    background: var(--paper);
    overflow: hidden;
  }
  .producer {
    position: absolute;
    top: 44px;
    left: 0;
    right: 0;
    text-align: center;
  }
  .producer-name {
    font-family: "Playfair Display", serif;
    font-weight: 700;
    font-size: 44px;
    color: var(--ink);
    line-height: 1;
  }
  .producer-range {
    margin-top: 10px;
    font-family: "Montserrat", sans-serif;
    font-weight: 500;
    font-size: 13px;
    letter-spacing: 0.42em;
    color: var(--ink);
  }
  .illustration {
    position: absolute;
    top: 150px;
    left: 90px;
    width: 430px;
    height: 280px;
    background: linear-gradient(180deg, var(--paper) 0%, var(--sketch-tone) 100%);
    border-radius: 6px;
  }
  .red-band {
    position: absolute;
    left: 0;
    bottom: 0;
    width: 600px;
    height: 330px;
  }
  .wine-name {
    position: absolute;
    left: 0;
    right: 0;
    top: 462px;
    text-align: center;
    font-family: "Sniglet", cursive;
    font-weight: 400;
    font-size: 100px;
    line-height: 1;
    color: var(--paper);
  }
  .vintage {
    position: absolute;
    left: 0;
    right: 0;
    top: 600px;
    text-align: center;
    font-family: "Playfair Display", serif;
    font-weight: 700;
    font-size: 28px;
    line-height: 1;
    color: var(--paper);
  }
  .wine-type {
    position: absolute;
    left: 0;
    right: 0;
    top: 650px;
    text-align: center;
    font-family: "Montserrat", sans-serif;
    font-weight: 500;
    font-size: 14px;
    letter-spacing: 0.42em;
    line-height: 1;
    color: var(--paper);
  }
</style>
</head>
<body>
  <main class="label">
    <header class="producer">
      <div class="producer-name">Tomás Arrabida</div>
      <div class="producer-range">WINES · VINHOS · VINS</div>
    </header>

    <div class="illustration" role="img" aria-label="Single-line drawing of a young woman drinking red wine from a glass, with red wine accents"></div>

    <svg class="red-band" viewBox="0 0 600 330" preserveAspectRatio="none" aria-hidden="true">
      <defs>
        <linearGradient id="bandGradient" x1="0" y1="0" x2="0" y2="1">
          <stop offset="0" stop-color="var(--wine-red)"/>
          <stop offset="1" stop-color="var(--wine-red-deep)"/>
        </linearGradient>
      </defs>
      <path d="M0 40 C 80 10, 150 30, 230 20 C 320 8, 380 40, 460 30 C 520 22, 570 40, 600 50 L600 330 L0 330 Z" fill="url(#bandGradient)"/>
    </svg>

    <h1 class="wine-name">Calvoreta</h1>
    <p class="vintage">2021</p>
    <p class="wine-type">RED WINE</p>
  </main>
</body>
</html>
```